New Business Card Design for Manufacturing

We are an engineering/manufacturing company that offers Advanced machining/assembly/engineering services, as well as innovative products for the heavy duty engine cooling markets.

We are looking to get a new business card designed that is clean and modern looking, but still fits the wide range of technical/skilled work we do.

- We hope to use this design as the base for other design work in new Presentations, web, and print work.

Industry/Entity Type

Engineering

Contact Information for Business Card

Our preferred color of blue is (RGB) 22/71/159 but can vary slightly from that color. Our content will be our Logo and full company name (Fabricated Tooling Works, Inc.), company address, name, job title, phone number with extension, cell number, fax number, website, and email address on the cards.
We'd like the full company name next to the logo, but we are open to other interpretations of that layout.
Preferably, we would like the back side to be clean with just our logo, and the front to contain all of the contact information.

Colors
2f74b4
0355a3
85abd2

Requirements
Must have
• - Logo, company name, needed content - We are open to interpretation beyond that.
• - Standard size business card.
• - Horizontal orientation.
• - Enough space for lengthy names / job titles (for example, a job title could read "Directory of Human Resources" or "V.P. of Governmental Affairs"). We need this to look clean, whether the title be short (CEO) or long (as described above).

```html
<!DOCTYPE html>
<html lang="en">
<head>
<meta charset="utf-8">
<title>Fabricated Tooling Works – Business Card</title>
<link href="https://fonts.googleapis.com/css2?family=Montserrat:wght@400;500;700;800&display=swap" rel="stylesheet">
<style>
  :root {
    --brand-blue: #0f4c99;
    --brand-blue-deep: #0b3f82;
    --brand-blue-soft: #2f74b4;
    --ink-grey: #6b6f75;
    --card-white: #f7f7f7;
    --backdrop: #e4e5e7;
  }
  * { box-sizing: border-box; margin: 0; padding: 0; }
  html, body {
    width: 1200px; height: 794px; overflow: hidden;
    background: var(--backdrop);
    font-family: "Montserrat", sans-serif;
  }
  .stage { position: relative; width: 1200px; height: 794px; }

  .card {
    position: absolute; width: 560px; height: 320px;
    box-shadow: 0 6px 14px rgba(0,0,0,0.12);
    overflow: hidden;
  }

  /* Back side */
  .card-back { left: 70px; top: 60px; background: var(--brand-blue); }
  .card-back .world-map {
    position: absolute; left: 60px; top: 40px; width: 440px; height: 200px;
    background: radial-gradient(ellipse at center, rgba(255,255,255,0.07), rgba(255,255,255,0) 70%);
  }
  .card-back .brand-name {
    position: absolute; left: 120px; top: 112px; width: 340px;
    color: #ffffff; font-weight: 800; font-size: 30px; line-height: 1.05;
    letter-spacing: 0.5px; text-transform: uppercase;
  }
  .card-back .website {
    position: absolute; left: 120px; top: 252px;
    color: rgba(255,255,255,0.6); font-size: 11px; letter-spacing: 0.8px;
  }

  /* Front side */
  .card-front { left: 570px; top: 414px; background: var(--card-white); }
  .card-front .brand-name {
    position: absolute; left: 40px; top: 44px; width: 300px;
    color: var(--brand-blue); font-weight: 800; font-size: 24px; line-height: 1.08;
    text-transform: uppercase; letter-spacing: 0.3px;
  }
  .card-front .accent-bar { position: absolute; width: 7px; background: var(--brand-blue); }
  .card-front .accent-bar.top-right { right: 0; top: 30px; height: 34px; }
  .card-front .accent-bar.bottom-left { left: 0; bottom: 30px; height: 86px; }

  .holder {
    position: absolute; right: 32px; top: 36px; text-align: right;
  }
  .holder .person-name { color: var(--brand-blue); font-weight: 700; font-size: 16px; letter-spacing: 0.5px; }
  .holder .job-title { color: var(--ink-grey); font-size: 9.5px; margin-top: 4px; }

  .address {
    position: absolute; right: 32px; top: 150px; text-align: right;
    color: var(--ink-grey); font-size: 10.5px; line-height: 1.6;
  }

  .contact-list {
    position: absolute; left: 34px; bottom: 30px; list-style: none;
    color: var(--ink-grey); font-size: 10.5px;
  }
  .contact-list li { display: flex; align-items: center; height: 17px; }
  .contact-list svg { width: 10px; height: 10px; margin-right: 9px; fill: var(--brand-blue); flex: none; }
</style>
</head>
<body>
<main class="stage">

  <section class="card card-back" aria-label="Business card back">
    <div class="world-map" role="img" aria-label="Faint world map in the background"></div>
    <div class="brand-name">Fabricated Tooling Works</div>
    <div class="website">www.ftworks-sample.com</div>
  </section>

  <section class="card card-front" aria-label="Business card front">
    <span class="accent-bar top-right"></span>
    <span class="accent-bar bottom-left"></span>

    <div class="brand-name">Fabricated Tooling Works</div>

    <div class="holder">
      <div class="person-name">MARCUS REED</div>
      <div class="job-title">President</div>
    </div>

    <div class="address">
      Street Name Avenue, Suite 100<br>
      State, Zip Code,Country
    </div>

    <ul class="contact-list">
      <li><svg viewBox="0 0 10 10"><path d="M2 0.5l1.8 2-1 1.2a6 6 0 0 0 3.5 3.5l1.2-1 2 1.8-1.3 1.6C4.5 9.4 0.6 5.5 0.4 1.8z"/></svg>+000.000.00.00</li>
      <li><svg viewBox="0 0 10 10"><path d="M2.5 0h5v10h-5zM3.5 1v7h3V1z"/></svg>+000.000.00.00</li>
      <li><svg viewBox="0 0 10 10"><path d="M2.5 0h5v3h-5zM0.5 3.5h9v4.5h-9zM2.5 7h5v3h-5z"/></svg>+000.000.00.00</li>
      <li><svg viewBox="0 0 10 10"><path d="M0 2h10v6H0zM0.8 2.6L5 5.6l4.2-3z" fill-rule="evenodd"/></svg>www.ftworks-sample.com</li>
      <li><svg viewBox="0 0 10 10"><path d="M5 0a5 5 0 1 0 0.01 0zM5 1.2a3.8 3.8 0 1 1-0.01 0zM4.5 1.2h1v7.6h-1zM1.2 4.5h7.6v1H1.2z"/></svg>www.ftworks-sample.com</li>
    </ul>
  </section>

</main>
</body>
</html>
```